TalkBridge - Language Coaching Services

Sleek, innovative, trendy design for Language Coaching business.

TalkBridge is a new UK based company that provides Language Coaching services. We offer highly personalized on-line and face to face language courses. We also impart learning techniques workshops based on the latest neuroscience research for second-language acquisition.

Target Market(s)

Industry/Entity Type

Consulting

Contact Information for Business Card

TalkBridge
ElenaVT@talkbridge-demo.co.uk
TalkBridge-demo.co.uk
Bristol, UK

Font styles to use
Sans Serif

```html
<!DOCTYPE html>
<html lang="en">
<head>
<meta charset="utf-8">
<title>TalkBridge – Business Card</title>
<link rel="stylesheet" href="https://fonts.googleapis.com/css2?family=Montserrat:wght@400;500;700&display=swap">
<style>
  :root {
    --bg: #2a2c30;
    --card-light: #ffffff;
    --card-dark: #141416;
    --brand-blue: #1e8fd0;
    --brand-deep: #2f6fb8;
    --text-blue: #3a78b8;
    --divider: #2a86c8;
  }
  * { margin: 0; padding: 0; box-sizing: border-box; }
  html, body { width: 1200px; height: 960px; overflow: hidden; }
  body {
    background: var(--bg);
    font-family: "Montserrat", sans-serif;
    display: flex;
    flex-direction: column;
    align-items: center;
    justify-content: center;
    gap: 60px;
  }
  .card {
    width: 700px;
    height: 400px;
    border-radius: 28px;
    position: relative;
    overflow: hidden;
  }
  .card-front {
    background: var(--card-light);
    display: flex;
    align-items: center;
    padding: 0 40px;
  }
  .card-back {
    background: var(--card-dark);
    display: flex;
    align-items: center;
    justify-content: center;
  }
  .brand {
    display: flex;
    flex-direction: column;
    align-items: center;
    gap: 18px;
  }
  .brand-mark {
    width: 90px;
    height: 90px;
    border-radius: 50%;
    border: 8px solid var(--brand-blue);
  }
  .brand-name {
    font-weight: 500;
    font-size: 30px;
    letter-spacing: 2px;
    color: var(--brand-blue);
    white-space: nowrap;
  }
  .card-back .brand-mark { border-color: var(--brand-deep); width: 120px; height: 120px; }
  .card-back .brand-name { color: var(--brand-deep); font-size: 48px; }
  .front-brand { width: 230px; flex: none; }
  .divider {
    width: 3px;
    height: 230px;
    background: var(--divider);
    margin: 0 26px 0 24px;
    flex: none;
  }
  .contact { color: var(--text-blue); }
  .contact-name {
    font-weight: 700;
    font-size: 28px;
    color: var(--brand-blue);
    letter-spacing: 0.5px;
  }
  .contact-title {
    font-weight: 400;
    font-size: 20px;
    margin-bottom: 16px;
  }
  .contact-list { list-style: none; }
  .contact-item {
    display: flex;
    align-items: center;
    gap: 10px;
    font-size: 15.5px;
    line-height: 34px;
    white-space: nowrap;
  }
  .contact-icon { width: 22px; height: 22px; flex: none; }
</style>
</head>
<body>
  <section class="card card-front">
    <div class="brand front-brand">
      <div class="brand-mark"></div>
      <div class="brand-name">TALKBRIDGE</div>
    </div>
    <div class="divider"></div>
    <div class="contact">
      <div class="contact-name">YOUR NAME</div>
      <div class="contact-title">YOUR TITLE</div>
      <ul class="contact-list">
        <li class="contact-item">
          <svg class="contact-icon" viewBox="0 0 24 24"><circle cx="12" cy="12" r="12" fill="#1e8fd0"/><path d="M12 5a4.5 4.5 0 0 0-4.5 4.5C7.5 13 12 19 12 19s4.5-6 4.5-9.5A4.5 4.5 0 0 0 12 5z" fill="#fff"/><circle cx="12" cy="9.5" r="1.7" fill="#1e8fd0"/></svg>
          Bristol, UK
        </li>
        <li class="contact-item">
          <svg class="contact-icon" viewBox="0 0 24 24"><circle cx="12" cy="12" r="12" fill="#1e8fd0"/><rect x="6" y="8" width="12" height="8.5" rx="1" fill="#fff"/><path d="M6.5 8.5 12 13l5.5-4.5" fill="none" stroke="#1e8fd0" stroke-width="1.2"/></svg>
          ElenaVT@talkbridge-demo.co.uk
        </li>
        <li class="contact-item">
          <svg class="contact-icon" viewBox="0 0 24 24"><circle cx="12" cy="12" r="12" fill="#1e8fd0"/><g fill="none" stroke="#fff" stroke-width="1.3"><circle cx="12" cy="12" r="6"/><ellipse cx="12" cy="12" rx="2.6" ry="6"/><path d="M6 12h12"/></g></svg>
          TalkBridge-demo.co.uk
        </li>
      </ul>
    </div>
  </section>

  <section class="card card-back">
    <div class="brand">
      <div class="brand-mark"></div>
      <div class="brand-name">TALKBRIDGE</div>
    </div>
  </section>
</body>
</html>
```